Web Design Project - veltrimo

I'm building an agency for marketing solutions but also medical education and patients education for pharmaceutical companies, medical societies and patient advocacy groups. We want to be perceived as the most innovative in the market. We work through design thinking solutions for campaigns and services.
I love some websites based on Swiss style design like www.plorvex.net
We are a small group of designers, physicians and creatives working together to deliver the best experiences in our market.
We decided to also use design crowd expecting that we maybe found a great idea we didn't thought about yet.
Updates

I'm extending it for more 2 weeks

Reason: I need the best design you can. Only PSD. No code needed. Love Swiss style, like qualdor 5 and plorvex.net I'm extending the deadline until get something great. Willing to extend as much as needed.

Target Market(s)

Pharmaceutical companies, physicians, medical societies, patients advocacy groups

Industry/Entity Type

Pharmaceutical

Font styles to use
Other font styles liked:
• Helvetia family

Colors

Designer to choose colors to be used in the design.

Requirements
Must have
• Must be innovative like www.plorvex.net
Nice to have
• Cool menus
Should not have
• Not to appear too much Comercial. We like to be a boutique in this market. Craftsmen working with less clients at time but delivering precious stones.

```html
<!DOCTYPE html>
<html lang="en">
<head>
<meta charset="utf-8">
<title>veltrimo</title>
<link rel="stylesheet" href="https://fonts.googleapis.com/css2?family=Arimo:wght@400;700&family=Source+Sans+3:wght@300;400;600&display=swap">
<style>
  :root {
    --teal: #00c2c4;
    --teal-light: #33d3d3;
    --white: #ffffff;
    --ink: #1f2a2a;
    --body: #555a5c;
    --band: rgba(60, 60, 60, 0.72);
    --label: rgba(20, 20, 20, 0.78);
    --dot: #2c2c2c;
  }
  * { box-sizing: border-box; margin: 0; padding: 0; }
  html, body { width: 1067px; height: 1200px; overflow: hidden; background: var(--white); }
  body { position: relative; font-family: "Arimo", Helvetica, Arial, sans-serif; }

  .site-header {
    position: absolute; left: 0; top: 0; width: 1067px; height: 64px;
    background: var(--teal);
    border-bottom: 3px solid var(--white);
    box-shadow: 0 2px 0 var(--teal);
  }
  .brand {
    position: absolute; left: 90px; top: 10px;
    font-size: 37px; font-weight: 400; color: var(--white); letter-spacing: 0.5px;
  }
  .main-nav { position: absolute; top: 0; left: 0; }
  .nav-item {
    position: absolute; top: 0; width: 68px; height: 62px;
    display: flex; align-items: center; justify-content: center;
  }
  .nav-item.is-active { background: var(--teal-light); }
  .nav-item svg { width: 42px; height: 42px; stroke: var(--ink); fill: none; stroke-width: 2.2; stroke-linejoin: round; stroke-linecap: round; }
  .nav-item.is-active svg { stroke: var(--white); }

  .hero {
    position: absolute; left: 0; top: 67px; width: 1067px; height: 353px;
    background: linear-gradient(135deg, #e9ecef 0%, #f7f8f9 40%, #d8dde2 70%, #3b4250 100%);
  }
  .hero-caption {
    position: absolute; left: 0; bottom: 0; width: 100%; height: 44px;
    background: var(--band);
  }
  .hero-caption p {
    position: absolute; left: 87px; top: 8px;
    color: var(--white); font-size: 25px;
  }
  .slider-dots { position: absolute; right: 90px; top: 16px; display: flex; gap: 10px; }
  .slider-dots span { width: 17px; height: 17px; border-radius: 50%; background: var(--dot); }
  .slider-dots span.is-current { background: var(--teal); }

  .tile { position: absolute; width: 239px; height: 187px; overflow: hidden; }
  .tile-photo { position: absolute; inset: 0; }
  .tile-label {
    position: absolute; left: 0; bottom: 0; width: 100%; height: 37px;
    background: var(--label); color: var(--white);
    font-weight: 700; font-size: 22px; letter-spacing: 0.4px;
    display: flex; align-items: center; justify-content: center;
  }
  .tile-patients { left: 90px; top: 473px; }
  .tile-patients .tile-photo { background: linear-gradient(150deg, #cfd6de 0%, #8b8f99 45%, #3a3d44 100%); }
  .tile-pharma { left: 90px; top: 689px; }
  .tile-pharma .tile-photo { background: linear-gradient(135deg, #e4e6ea 0%, #c9a25a 35%, #c43a2a 55%, #cfe4e8 80%, #f0f0f0 100%); }
  .tile-marketing { left: 739px; top: 473px; }
  .tile-marketing .tile-photo { background: linear-gradient(135deg, #f2f3f5 0%, #dfe2e6 50%, #6e7480 100%); }
  .tile-medical { left: 738px; top: 689px; }
  .tile-medical .tile-photo { background: linear-gradient(135deg, #e8ede9 0%, #8a6a55 40%, #4a79b8 75%, #2e3a55 100%); }

  .welcome {
    position: absolute; left: 350px; top: 474px; width: 367px; height: 402px;
    background: var(--teal); padding: 12px 12px 0 16px;
  }
  .welcome h1 { font-weight: 400; color: var(--white); font-size: 30px; letter-spacing: -0.5px; }
  .welcome h1 .name { color: var(--ink); font-size: 40px; margin-left: 6px; }
  .welcome p {
    margin-top: 4px; padding-left: 4px;
    font-family: "Source Sans 3", "Source Sans Pro", sans-serif; font-weight: 300;
    color: var(--white); font-size: 26px; line-height: 41px; letter-spacing: 1.1px;
  }
  .welcome p strong { font-weight: 600; }

  .societies-photo {
    position: absolute; left: 89px; top: 927px; width: 282px; height: 198px;
    background: linear-gradient(120deg, #e9e3dc 0%, #d9c7b5 30%, #f4f4f4 55%, #7fb3d9 85%, #c9d8e6 100%);
  }
  .societies {
    position: absolute; left: 417px; top: 918px; width: 565px;
    font-family: "Source Sans 3", "Source Sans Pro", sans-serif; font-weight: 300;
  }
  .societies h2 { font-weight: 300; color: var(--teal); font-size: 50px; letter-spacing: 2px; line-height: 56px; }
  .societies p { margin-top: 6px; color: var(--body); font-size: 25px; line-height: 35.6px; letter-spacing: 1px; }

  .site-footer {
    position: absolute; left: 0; top: 1163px; width: 1067px; height: 37px;
    background: var(--teal); color: var(--white);
    font-size: 13.5px; display: flex; align-items: center; justify-content: center;
  }
</style>
</head>
<body>
  <header class="site-header">
    <div class="brand">veltrimo</div>
    <nav class="main-nav">
      <a class="nav-item is-active" style="left:533px">
        <svg viewBox="0 0 42 42"><path d="M5 21 L21 6 L37 21"/><path d="M10 17 V37 H18 V27 H24 V37 H32 V17"/></svg>
      </a>
      <a class="nav-item" style="left:634px">
        <svg viewBox="0 0 42 42"><rect x="4" y="11" width="34" height="25" rx="3"/><path d="M15 11 V6 H27 V11"/><path d="M21 17 V31 M14 24 H28" stroke-width="3"/></svg>
      </a>
      <a class="nav-item" style="left:731px">
        <svg viewBox="0 0 42 42"><path d="M14 20 a7 7 0 1 1 14 0 c0 4 -3 5 -3 9 h-8 c0 -4 -3 -5 -3 -9z"/><path d="M17 32 H25 M18 35 H24"/><path d="M18 20 L21 24 L24 20"/><path d="M21 4 V7 M8 9 L10 11 M34 9 L32 11 M4 20 H7 M35 20 H38"/></svg>
      </a>
      <a class="nav-item" style="left:818px">
        <svg viewBox="0 0 42 42"><rect x="14" y="4" width="14" height="6" rx="1"/><path d="M15 10 L12 15 V37 H30 V15 L27 10"/><path d="M21 20 V30 M16 25 H26"/></svg>
      </a>
      <a class="nav-item" style="left:927px">
        <svg viewBox="0 0 42 42"><rect x="5" y="10" width="32" height="22" rx="3"/><circle cx="15" cy="19" r="3"/><path d="M10 27 c1 -4 9 -4 10 0"/><circle cx="28" cy="20" r="4"/><path d="M32 20 v2"/><path d="M10 32 V35 M32 32 V35"/></svg>
      </a>
    </nav>
  </header>

  <section class="hero" role="img" aria-label="Photo of a business team at a table reviewing charts on a clipboard, with coffee cups and papers">
    <div class="hero-caption">
      <p>Lorem ipsum dolor sit amet.</p>
      <div class="slider-dots"><span class="is-current"></span><span></span><span></span></div>
    </div>
  </section>

  <a class="tile tile-patients">
    <div class="tile-photo" role="img" aria-label="Photo of a woman working on a laptop"></div>
    <div class="tile-label">Patients Education</div>
  </a>
  <a class="tile tile-pharma">
    <div class="tile-photo" role="img" aria-label="Photo of assorted pills and capsules"></div>
    <div class="tile-label">Pharmaceutical</div>
  </a>

  <section class="welcome">
    <h1>welcome to<span class="name">veltrimo</span></h1>
    <p>simply dummy text of the printing and typesetting in&shy;dustry. <strong>Lorem Ipsum</strong> has been the industry's stan&shy;dard dummy text ever since the 1500s, when an un&shy;known printer took a galley.</p>
  </section>

  <a class="tile tile-marketing">
    <div class="tile-photo" role="img" aria-label="Photo of a team discussing charts at a table"></div>
    <div class="tile-label">Marketing Solutions</div>
  </a>
  <a class="tile tile-medical">
    <div class="tile-photo" role="img" aria-label="Photo of students in a classroom"></div>
    <div class="tile-label">Medical Education</div>
  </a>

  <div class="societies-photo" role="img" aria-label="Photo of a group of smiling doctors and nurses"></div>
  <section class="societies">
    <h2>Medical societies</h2>
    <p>simply dummy text of the printing and typeset&shy;ting industry. Lorem Ipsum has been the in&shy;dustry's standard dummy text ever since the 1500s, when an unknown a galley.</p>
  </section>

  <footer class="site-footer">©&nbsp; 2014 veltrimo. All Rights Reserved | Privacy Policy</footer>
</body>
</html>
```